Business Card Design Project Lend Aid

Simple and clean business card,

Logo and fond added in attachment

Data need to be changable:
Ria Vondeck
Customer Service Specialist

Lend Aid - ria.vondeck@lendaid.be - Mob: +32491532876 - www.lendaid.be

Target Market(s)

Small businesses

Industry/Entity Type

Business

Requirements
Nice to have
• QR-code

```html
<!DOCTYPE html>
<html lang="en">
<head>
<meta charset="utf-8">
<title>Lend Aid – Business Card</title>
<link rel="stylesheet" href="https://fonts.googleapis.com/css2?family=Signika:wght@400;500&display=swap">
<style>
  :root{
    --page:#ffffff;
    --card:#ffffff;
    --card-edge:#bdbdbd;
    --leaf-light:#dfe9be;
    --leaf-dark:#d0cea2;
    --ink:#111111;
    --brand-green:#86c140;
    --brand-blue:#29a9e1;
  }
  html,body{margin:0;padding:0;width:1200px;height:1000px;overflow:hidden;background:var(--page);}
  .canvas{position:relative;width:1200px;height:1000px;font-family:"Signika",sans-serif;color:var(--ink);}
  .card{position:absolute;left:193px;top:163px;width:814px;height:464px;background:var(--card);border:1px solid var(--card-edge);box-sizing:border-box;}
  .card-shapes{position:absolute;left:0;top:0;}
  .brand{position:absolute;left:658px;top:216px;display:flex;align-items:center;gap:12px;}
  .brand-mark{width:40px;height:40px;background:var(--brand-blue);border-radius:6px;}
  .brand-name{font-size:44px;font-weight:500;color:var(--brand-green);line-height:1;}
  .person-name{position:absolute;left:276px;top:316px;margin:0;font-size:52px;font-weight:500;line-height:1;}
  .person-role{position:absolute;left:273px;top:420px;margin:0;font-size:31px;font-weight:400;line-height:1;}
  .contact{position:absolute;font-size:30px;line-height:1;display:flex;align-items:center;}
  .contact svg{flex:none;}
  .contact-email{left:227px;top:504px;gap:22px;}
  .contact-phone{left:229px;top:555px;gap:20px;}
  .contact-web{left:508px;top:555px;gap:20px;}
</style>
</head>
<body>
<div class="canvas">
  <div class="card"></div>
  <svg class="card-shapes" width="1200" height="1000" viewBox="0 0 1200 1000" aria-hidden="true">
    <path fill="var(--leaf-light)" d="M220,360 C220,260 300,190 420,190 L980,190 L980,330 C980,362 956,385 922,385 L292,385 C252,385 226,400 220,422 Z"/>
    <path fill="var(--leaf-dark)" d="M220,446 C226,420 250,405 292,405 L922,405 C956,405 978,386 980,360 L980,420 C980,520 900,600 790,600 L220,600 Z"/>
  </svg>

  <div class="brand">
    <span class="brand-mark"></span>
    <span class="brand-name">Lend Aid</span>
  </div>

  <h1 class="person-name">Ria Vondeck</h1>
  <p class="person-role">Customer Service Specialist</p>

  <div class="contact contact-email">
    <svg width="31" height="22" viewBox="0 0 31 22" aria-hidden="true">
      <rect x="0" y="0" width="31" height="22" fill="#111"/>
      <path d="M2,2 L15.5,13 L29,2" fill="none" stroke="var(--leaf-dark)" stroke-width="2"/>
      <path d="M2,20 L11,10 M29,20 L20,10" stroke="var(--leaf-dark)" stroke-width="2"/>
    </svg>
    <span>ria.vondeck@lendaid.be</span>
  </div>

  <div class="contact contact-phone">
    <svg width="22" height="38" viewBox="0 0 22 38" aria-hidden="true">
      <rect x="0" y="0" width="22" height="38" rx="4" fill="#111"/>
      <rect x="3" y="5" width="16" height="25" fill="var(--leaf-dark)"/>
      <circle cx="11" cy="34" r="1.8" fill="var(--leaf-dark)"/>
    </svg>
    <span>+32491532876</span>
  </div>

  <div class="contact contact-web">
    <svg width="40" height="40" viewBox="0 0 40 40" aria-hidden="true">
      <circle cx="20" cy="20" r="20" fill="#111"/>
      <path d="M9,12 C14,9 18,12 17,16 C16,20 12,19 11,23 C10,27 8,26 7,22 C6,18 6,14 9,12 Z" fill="var(--leaf-dark)"/>
      <path d="M24,8 C29,9 33,13 32,18 C31,22 27,20 25,24 C23,29 26,32 22,33 C20,29 21,25 19,22 C17,19 22,17 23,14 C24,12 21,10 24,8 Z" fill="var(--leaf-dark)"/>
    </svg>
    <span>www.lendaid.be</span>
  </div>
</div>
</body>
</html>
```